チラシに使用する文章と画像はこちらで用意いたします。
全体の雰囲気はimageBのような感じです。
作りたいチラシのイメージはimageAのとおりです。
デザインは自由に調整いただいてかまいません。
使用する色はimageBのような「黒、茶」を考えておりますが、自由に調整いただいて結構です。

使用する文章はPDFファイルを参照下さい。
imageAのAからIはPDFの文章を入れて下さい。

imageAのDにいれる画像は「health.zip」をご使用下さい。
imageAのEにいれる画像は「urinary organs.zip」をご使用下さい。
imageAのFにいれる画像は「digestive organs.zip」をご使用下さい。
画像はimageBのように並べて下さい。

またimageAのD、E、Fのハーブの画像の上に「ORU・PLANTIVA」のマークを入れて下さい。
詳しくはimageAをご参照ください。
マークの画像はimageCをお使い下さい。
有機農作物はマークがないため、有機農作物と記載して下さい。
A4
片面
黒 茶色
• 高解像度JPG (.jpg)
• イラストレーター形式 (.ai)

柔らかい雰囲気やデザインなどとても気に入りました。
色合いも落ち着いているので、読みやすかったです。

たくさん提案くださり、誠にありがとうございます。
また機会があれば、どうぞよろしくお願い致します。

```html
<!DOCTYPE html>
<html lang="ja">
<head>
<meta charset="utf-8">
<title>ペットのためのハーブ</title>
<link href="https://fonts.googleapis.com/css2?family=Shippori+Mincho:wght@500;700&family=Noto+Sans+JP:wght@400;500&display=swap" rel="stylesheet">
<style>
:root{
  --ink:#3a2a20;
  --brown:#4a3528;
  --brown-dark:#3b2a20;
  --paper:#efe9e0;
  --panel:#f8f5f0;
  --line:#b8a898;
  --muted:#6a5a4e;
  --accent:#8a6a4e;
}
*{margin:0;padding:0;box-sizing:border-box}
html,body{width:849px;height:1200px;overflow:hidden}
body{background:var(--paper);font-family:"Noto Sans JP",sans-serif;color:var(--ink);position:relative}
.header{position:absolute;left:0;top:0;width:849px;height:178px;background:linear-gradient(180deg,var(--brown) 0%,var(--brown-dark) 100%)}
.header .pets{position:absolute;left:30px;top:30px;width:789px;height:140px;background:linear-gradient(90deg,rgba(255,255,255,.06),rgba(255,255,255,.02),rgba(255,255,255,.06))}
.header h1{position:absolute;left:0;right:0;top:30px;text-align:center;font-family:"Shippori Mincho",serif;font-weight:700;color:#fff;font-size:38px;line-height:54px;letter-spacing:2px}
.panel{position:absolute;background:var(--panel);border:1px solid #d9cfc3}
.intro{left:50px;top:198px;width:372px;height:210px;padding:16px 18px}
.intro h2{font-family:"Shippori Mincho",serif;font-size:19px;line-height:30px;border-left:2px solid var(--brown);padding-left:14px;margin:6px 0 12px 6px}
.intro p,.feature p{font-size:9px;line-height:15px;color:var(--muted)}
.feature{left:438px;width:362px;padding:10px 16px}
.feature h3{font-family:"Shippori Mincho",serif;font-size:15px;font-weight:700;border-bottom:1px solid var(--line);padding-bottom:5px;margin-bottom:6px}
.f1{top:198px;height:96px}
.f2{top:304px;height:104px}
.product{position:absolute;left:50px;width:750px;height:186px;border-top:1px solid var(--line);padding-top:12px;display:flex}
.product .desc{width:170px;flex:none}
.product h4{font-family:"Shippori Mincho",serif;font-size:13px;font-weight:700}
.product .price{font-size:10px;color:var(--accent);margin:2px 0 6px}
.product .desc p{font-size:8px;line-height:13px;color:var(--muted)}
.herbs{display:grid;grid-template-columns:repeat(5,1fr);grid-auto-rows:76px;column-gap:8px;row-gap:8px;align-content:start;flex:1;padding-left:18px}
.herb{text-align:center;display:flex;flex-direction:column;align-items:center}
.mark{font-size:7px;line-height:12px;color:var(--ink);height:12px;display:flex;align-items:center;justify-content:center;gap:3px;white-space:nowrap}
.mark i{display:inline-block;width:7px;height:7px;border:1px solid var(--ink)}
.herb .photo{width:46px;height:46px;border-radius:4px;margin:2px 0 3px}
.herb span{font-size:7.5px;line-height:12px;color:var(--muted);white-space:nowrap}
.g{background:radial-gradient(circle at 40% 40%,#9a9a7a,#5e5e44)}
.y{background:radial-gradient(circle at 40% 40%,#e2d6a6,#b29a64)}
.r{background:radial-gradient(circle at 40% 40%,#8a5a56,#4a2e30)}
.b{background:radial-gradient(circle at 40% 40%,#a88a6a,#6a4e38)}
.p1{top:436px}.p2{top:630px}.p3{top:824px}
.certs{position:absolute;left:50px;top:1030px;width:750px;display:flex;gap:10px}
.cert{flex:1;height:70px;background:var(--panel);border:1px solid #d9cfc3;display:flex;align-items:center;gap:8px;padding:6px 10px}
.cert .badge{width:40px;height:40px;border-radius:50%;background:#cbbfb0;flex:none}
.cert b{font-size:9px;display:block;margin-bottom:2px}
.cert p{font-size:7.5px;line-height:11px;color:var(--muted)}
</style>
</head>
<body>
<header class="header">
  <div class="pets" role="img" aria-label="猫と犬のシルエット"></div>
  <h1>大切な家族だから<br>いつも若々しく元気でいてほしい</h1>
</header>

<section class="panel intro">
  <h2>現代の犬、猫にこそ<br>ハーブをおすすめします。</h2>
  <p>大や猫が野生の肉食獣だった頃、獲物の内臓を一緒に食べていたと言います。なぜなら獲物が食べた草食動物の胃の中には、消化された植物が入っていたからです。<br>現代に生きるペットは、家ごもり等で運動不足が大きな課題です。そこで毎日の食事に植物の力を少し加えることで、健やかな体づくりを応援します。</p>
</section>
<section class="panel feature f1">
  <h3>特筆すべきは抗酸化作用</h3>
  <p>「酸化」は、老化や病気を引き起こす原因のひとつと言われています。ハーブに含まれる成分は体のサビを防ぎ、毎日の若々しさを保つお手伝いをします。</p>
</section>
<section class="panel feature f2">
  <h3>腸内環境を整える</h3>
  <p>体に良いものを食べても消化吸収がうまくできなければ意味がありません。ハーブは腸の働きを助け、便通を良くし、体の内側から健康を支えます。自然の恵みを安心してお与えください。</p>
</section>

<section class="product p1">
  <div class="desc"><h4>健康増進応援ハーブ</h4><div class="price">25g入り　1,260円</div><p>毎日の食事に少量加えるだけで、体の調子を整え、元気な毎日を応援するブレンドです。抗酸化作用のあるハーブを厳選し、シニア期のペットにもおすすめです。</p></div>
  <div class="herbs">
    <div class="herb"><div class="mark"><i></i>ORU・PLANTIVA</div><div class="photo g" role="img" aria-label="ハーブの写真"></div><span>ペパーミント</span></div>
    <div class="herb"><div class="mark"><i></i>ORU・PLANTIVA</div><div class="photo b" role="img" aria-label="ハーブの写真"></div><span>ダンデライオン</span></div>
    <div class="herb"><div class="mark"><i></i>ORU・PLANTIVA</div><div class="photo r" role="img" aria-label="ハーブの写真"></div><span>ローズヒップ</span></div>
    <div class="herb"><div class="mark"><i></i>ORU・PLANTIVA</div><div class="photo g" role="img" aria-label="ハーブの写真"></div><span>ネトル</span></div>
    <div class="herb"><div class="mark">有機農作物</div><div class="photo y" role="img" aria-label="ハーブの写真"></div><span>ターメリック</span></div>
    <div class="herb"><div class="mark"><i></i>ORU・PLANTIVA</div><div class="photo g" role="img" aria-label="ハーブの写真"></div><span>パセリ</span></div>
    <div class="herb"><div class="mark"><i></i>ORU・PLANTIVA</div><div class="photo y" role="img" aria-label="ハーブの写真"></div><span>カモミール</span></div>
    <div class="herb"><div class="mark"><i></i>ORU・PLANTIVA</div><div class="photo g" role="img" aria-label="ハーブの写真"></div><span>タイム</span></div>
    <div class="herb"><div class="mark">有機農作物</div><div class="photo b" role="img" aria-label="ハーブの写真"></div><span>ジンジャー</span></div>
  </div>
</section>

<section class="product p2">
  <div class="desc"><h4>泌尿器系応援ハーブ</h4><div class="price">25g入り　1,260円</div><p>水分の巡りを助け、健やかな泌尿器の働きをサポートします。毎日のお水やごはんに混ぜて与えやすい、やさしいブレンドです。</p></div>
  <div class="herbs">
    <div class="herb"><div class="mark"><i></i>ORU・PLANTIVA</div><div class="photo g" role="img" aria-label="ハーブの写真"></div><span>スギナ</span></div>
    <div class="herb"><div class="mark"><i></i>ORU・PLANTIVA</div><div class="photo y" role="img" aria-label="ハーブの写真"></div><span>コーンシルク</span></div>
    <div class="herb"><div class="mark"><i></i>ORU・PLANTIVA</div><div class="photo g" role="img" aria-label="ハーブの写真"></div><span>ネトル</span></div>
    <div class="herb"><div class="mark">有機農作物</div><div class="photo b" role="img" aria-label="ハーブの写真"></div><span>ダンデライオン</span></div>
    <div class="herb"><div class="mark"><i></i>ORU・PLANTIVA</div><div class="photo r" role="img" aria-label="ハーブの写真"></div><span>クランベリー</span></div>
    <div class="herb"><div class="mark"><i></i>ORU・PLANTIVA</div><div class="photo g" role="img" aria-label="ハーブの写真"></div><span>パセリ</span></div>
    <div class="herb"><div class="mark"><i></i>ORU・PLANTIVA</div><div class="photo y" role="img" aria-label="ハーブの写真"></div><span>マシュマロウ</span></div>
  </div>
</section>

<section class="product p3">
  <div class="desc"><h4>消化器系応援ハーブ</h4><div class="price">25g入り　1,260円</div><p>胃腸の働きを穏やかに整え、消化吸収をサポートします。食欲が落ちがちな時期や、お腹の調子が気になる子におすすめです。</p></div>
  <div class="herbs">
    <div class="herb"><div class="mark"><i></i>ORU・PLANTIVA</div><div class="photo g" role="img" aria-label="ハーブの写真"></div><span>ペパーミント</span></div>
    <div class="herb"><div class="mark"><i></i>ORU・PLANTIVA</div><div class="photo y" role="img" aria-label="ハーブの写真"></div><span>カモミール</span></div>
    <div class="herb"><div class="mark"><i></i>ORU・PLANTIVA</div><div class="photo g" role="img" aria-label="ハーブの写真"></div><span>フェンネル</span></div>
    <div class="herb"><div class="mark">有機農作物</div><div class="photo b" role="img" aria-label="ハーブの写真"></div><span>ジンジャー</span></div>
    <div class="herb"><div class="mark"><i></i>ORU・PLANTIVA</div><div class="photo y" role="img" aria-label="ハーブの写真"></div><span>スリッパリーエルム</span></div>
    <div class="herb"><div class="mark"><i></i>ORU・PLANTIVA</div><div class="photo g" role="img" aria-label="ハーブの写真"></div><span>レモンバーム</span></div>
    <div class="herb"><div class="mark"><i></i>ORU・PLANTIVA</div><div class="photo b" role="img" aria-label="ハーブの写真"></div><span>リコリス</span></div>
    <div class="herb"><div class="mark"><i></i>ORU・PLANTIVA</div><div class="photo g" role="img" aria-label="ハーブの写真"></div><span>タイム</span></div>
    <div class="herb"><div class="mark">有機農作物</div><div class="photo y" role="img" aria-label="ハーブの写真"></div><span>キャラウェイ</span></div>
  </div>
</section>

<footer class="certs">
  <div class="cert"><div class="badge"></div><div><b>有機ハーブ（ORU・PLANTIVA マーク）</b><p>認証機関の基準に適合した、農薬や化学肥料に頼らず育てた原料です。</p></div></div>
  <div class="cert"><div class="badge"></div><div><b>農薬不使用ハーブ</b><p>栽培期間中に農薬を使用せず、自然に近い環境で育てた原料です。</p></div></div>
  <div class="cert"><div class="badge"></div><div><b>有機農作物</b><p>認証マークはありませんが、有機栽培で育てられた原料を使用しています。</p></div></div>
</footer>
</body>
</html>
```